Wedding Brochure/Booklet for Fern & The Heron

We have the content and a previous attempt already. We just need some edits and then have a version we can email as a PDF and Print as a Booklet.

Any further improvements to the visual aspect would also be welcomed

Check out our website to see who we are www.fernandtheheron-example.com

Target Market(s)

Couples!!!!

Industry/Entity Type

Wedding

Font styles to use
Sans Serif
Decorative
Script

Requirements
Must have
• Style
Nice to have
• Style & Elegance
Should not have
• Too bold or Bright Colours

```html
<!DOCTYPE html>
<html lang="en">
<head>
<meta charset="utf-8">
<title>Fern &amp; The Heron — Wedding Packages</title>
<link rel="stylesheet" href="https://fonts.googleapis.com/css2?family=Poiret+One&family=Quicksand:wght@600&family=Open+Sans:wght@400&display=swap">
<style>
  :root {
    --bg: #d0d0d0;
    --page: #ffffff;
    --blush: #fde4d9;
    --blush-edge: #f3d6cb;
    --ink: #857876;
    --ink-strong: #6c6265;
    --ornament: #4a3a40;
    --url: #8a8a8a;
  }
  * { box-sizing: border-box; margin: 0; padding: 0; }
  html, body { width: 1200px; height: 1200px; overflow: hidden; }
  body {
    background: var(--bg);
    position: relative;
    font-family: "Poiret One", "Quicksand", sans-serif;
    color: var(--ink);
  }
  .spread {
    position: absolute;
    left: 112px; top: 238px;
    display: flex;
  }
  .page {
    width: 488px; height: 724px;
    background: var(--page);
    position: relative;
  }
  .panel {
    position: absolute;
    left: 46px; top: 44px;
    width: 406px; height: 644px;
    background: linear-gradient(90deg, var(--blush) 0%, var(--blush) 75%, var(--blush-edge) 100%);
    display: flex; flex-direction: column; align-items: center;
    text-align: center;
  }
  .page--right .panel {
    background: linear-gradient(90deg, var(--blush-edge) 0%, var(--blush) 20%, var(--blush) 100%);
  }
  .ornament {
    width: 112px; height: 14px;
    background: var(--ornament);
    opacity: .35;
    border-radius: 7px;
    flex: none;
  }
  .ornament--top { margin-top: 15px; }
  .ornament--bottom { margin-top: auto; margin-bottom: 22px; }
  .package-title {
    font-weight: 400;
    font-size: 23px;
    color: var(--ink-strong);
    letter-spacing: .3px;
    line-height: 30px;
  }
  .package-title--bold {
    font-family: "Quicksand", sans-serif;
    font-weight: 600;
    font-size: 16px;
    line-height: 26px;
  }
  .package-sub {
    font-size: 14px;
    line-height: 20px;
    margin-bottom: 10px;
  }
  .package-items {
    list-style: none;
    font-size: 13.2px;
    line-height: 22px;
    width: 270px;
  }
  .url {
    position: absolute;
    left: 0; right: 0; top: 701px;
    text-align: center;
    font-family: "Open Sans", sans-serif;
    font-size: 12.8px;
    color: var(--url);
  }
</style>
</head>
<body>
  <main class="spread">
    <section class="page page--left">
      <div class="panel">
        <div class="ornament ornament--top" role="img" aria-label="Small decorative flourish divider"></div>

        <h2 class="package-title" style="margin-top:12px">Old Willowbank House</h2>
        <p class="package-sub">Champagne at Ceremony</p>
        <ul class="package-items" style="width:300px">
          <li>Antipasto Grazing Tables</li>
          <li>3 Canapes - Heron Canape Menu</li>
          <li>Dinner - 2 Choices, Alternate DropSteamed</li>
          <li>Seasonal Greens accompany Main Meals</li>
          <li>Wedding Cake Served as dessert</li>
          <li>4.5hr Beverage Package</li>
          <li>$160 p/p</li>
        </ul>

        <h2 class="package-title package-title--bold" style="margin-top:20px">The Ashcombe</h2>
        <p class="package-sub" style="margin-bottom:14px">Champagne at Ceremony</p>
        <ul class="package-items">
          <li>Antipasto Grazing Table</li>
          <li>Aussie Seafood Station</li>
          <li>6 Canapes (Fern Canape Menu)</li>
          <li>Dinner (3 Choices, Alternate Drop)</li>
          <li>Steamed Seasonal Greens accompany Main Meals</li>
          <li>Your Wedding Cake Served as Dessert</li>
          <li>Petite Tarts</li>
          <li>Cheese Platter</li>
          <li>4.5hr Beverage Package</li>
          <li>$195</li>
        </ul>

        <div class="ornament ornament--bottom" role="img" aria-label="Small decorative flourish divider"></div>
      </div>
      <p class="url">www.fernandtheheron-example.com</p>
    </section>

    <section class="page page--right">
      <div class="panel">
        <div class="ornament ornament--top" role="img" aria-label="Small decorative flourish divider"></div>

        <h2 class="package-title" style="margin-top:26px;margin-bottom:14px">The Great Aussie BBQ Wedding</h2>
        <ul class="package-items">
          <li>Antipasto Grazing Table</li>
          <li>Aussie Seafood Station</li>
          <li>3 Canapes (Fern Canape Menu)</li>
          <li>Aussie BBQ</li>
          <li>(Insert actual BBQ Menu Here)</li>
          <li>Petite Tarts</li>
          <li>Cheese Platter</li>
          <li>4.5hr Beverage Package</li>
          <li>$175 p/p Minimum</li>
        </ul>

        <h2 class="package-title" style="margin-top:70px;margin-bottom:14px">Small Wedding</h2>
        <ul class="package-items">
          <li>Antipasto Grazing Station</li>
          <li>5 Canapes (Heron Canape Selection)</li>
          <li>Wedding Cake Served as dessert</li>
          <li>Tea &amp; Coffee Station</li>
          <li>2.5hr Beverage Package</li>
          <li>Max 40 Guests</li>
        </ul>

        <div class="ornament ornament--bottom" role="img" aria-label="Small decorative flourish divider"></div>
      </div>
      <p class="url">www.fernandtheheron-example.com</p>
    </section>
  </main>
</body>
</html>
```